A creative, unique invitation card for destination wedding

We are looking for a creative wedding invitation card for our destination wedding at Koh Samui. Wedding theme colour is in blue grey (slate blue) and khaki. We have included the one idea we have for the wedding invite (please ignore the fonts and colour). However, we would love to explore more unqiue ideas and design. Please include the photos attached and feel free to choose between the duplicates.

Target Market(s)

Friends and families

Industry/Entity Type

Wedding

Font styles to use
Sans Serif
Decorative
Script

Colors

Designer to choose colors to be used in the design.

Requirements
Must have
• Card should fit into a 110 X 220 cm envelope
Nice to have
• One design with blue grey/slate blue colour palette
Should not have
• Avoid dye cut
• Cartoons
• Primary colours

```html
<!DOCTYPE html>
<html lang="en">
<head>
<meta charset="utf-8">
<title>Destination Wedding Invitation</title>
<link rel="stylesheet" href="https://fonts.googleapis.com/css2?family=Poiret+One&family=Playfair+Display+SC&family=Courier+Prime:wght@700&display=swap">
<style>
  :root {
    --page: #ffffff;
    --slate: #9bb0bd;
    --charcoal: #3a3c3e;
    --ice: #a9c2d2;
    --white: #ffffff;
    --ink: #2f3336;
    --photo-top: #efe9dc;
    --photo-mid: #bccbd0;
    --photo-low: #c9ab9a;
    --photo-base: #d29a7e;
  }
  * { box-sizing: border-box; margin: 0; padding: 0; }
  html, body { width: 1200px; height: 1200px; overflow: hidden; background: var(--page); }
  .invitation {
    position: absolute; left: 326px; top: 58px;
    width: 540px; height: 1080px;
    background: var(--slate);
    overflow: hidden;
  }
  .photo {
    position: absolute; left: 0; top: 0; width: 540px; height: 702px;
    background: linear-gradient(180deg, var(--photo-top) 0%, var(--photo-mid) 40%, var(--photo-low) 75%, var(--photo-base) 100%);
  }
  .frame {
    position: absolute; left: 24px; top: 25px; right: 24px; bottom: 26px;
    border: 2px solid var(--white);
  }
  .title {
    position: absolute; left: 0; width: 100%; text-align: center;
    font-family: "Poiret One", sans-serif; font-weight: 400; color: var(--white);
    line-height: 1;
  }
  .title--our { top: 278px; font-size: 54px; letter-spacing: 2px; }
  .title--wedding { top: 344px; font-size: 80px; letter-spacing: -2px; transform: scaleX(0.77); }
  .names-banner {
    position: absolute; left: 88px; top: 684px; width: 362px; height: 68px;
    background: var(--charcoal);
    border: 1px solid #777;
    display: flex; align-items: center; justify-content: center; gap: 10px;
    font-family: "Playfair Display SC", serif; color: var(--ice);
  }
  .names-banner .name { font-size: 40px; }
  .names-banner .and { font-size: 22px; color: var(--white); }
  .banner-rule { position: absolute; left: 88px; width: 362px; background: var(--charcoal); }
  .banner-rule--a { top: 755px; height: 2px; }
  .banner-rule--b { top: 760px; height: 1px; }
  .copy {
    position: absolute; left: 0; width: 100%; text-align: center;
    font-family: "Courier Prime", monospace; font-weight: 700; color: var(--white);
    line-height: 1.2;
  }
  .copy--lead { top: 815px; font-size: 17px; letter-spacing: 0.6px; }
  .copy--sub { top: 847px; font-size: 17px; letter-spacing: 0.6px; }
  .date {
    position: absolute; top: 895px; left: 0; width: 100%;
    display: flex; justify-content: center; align-items: center; gap: 6px;
    font-family: "Courier Prime", monospace; font-weight: 700; color: var(--white);
    font-size: 32px; letter-spacing: 2px;
  }
  .date .day {
    width: 58px; height: 58px; border-radius: 50%;
    background: var(--charcoal); border: 2px solid var(--white);
    display: flex; align-items: center; justify-content: center;
    color: var(--ice); letter-spacing: 1px;
  }
  .copy--place { top: 956px; font-size: 17px; letter-spacing: 1px; }
  .copy--rsvp { top: 1021px; font-size: 17px; letter-spacing: 1.2px; color: var(--ink); }
</style>
</head>
<body>
  <main class="invitation">
    <div class="photo" role="img" aria-label="Photo of the couple holding hands by the sea, engagement ring in focus"></div>
    <div class="frame"></div>
    <h1 class="title title--our">OUR</h1>
    <h1 class="title title--wedding">WEDDING</h1>
    <div class="names-banner">
      <span class="name">LOREM</span><span class="and">AND</span><span class="name">IPSUM</span>
    </div>
    <div class="banner-rule banner-rule--a"></div>
    <div class="banner-rule banner-rule--b"></div>
    <p class="copy copy--lead">Are getting married</p>
    <p class="copy copy--sub">Come away with us to celebrate this union</p>
    <p class="date"><span>JUNE</span><span class="day">21</span><span>2018</span></p>
    <p class="copy copy--place">Koh Samui</p>
    <p class="copy copy--rsvp">RSVP -555-0142</p>
  </main>
</body>
</html>
```